Pinecrest Renovations - Get the creative juices going!!

Pinecrest does not do the actual renovation work. The company provides high end project management of renovation (primarily residential - with an eye toward commercial) The renovation work could look very different between projects. This company manages the work of contractors, architects and interior designers (either subcontracted directly by Pinecrest or hired by the client and entrusted to Pinecrest to manage). Clients are high end in the economic scale and the card needs to have a high end feel to it.

The owner is female, but the audience will be heavily slanted male. It should not be a "feminine" or "masculine" looking card. If anything, slant more on the masculine side. Clean, simple, yet creative and artistically appealing. The card design should complement and in no way compete with the logo.

When people think of our company: trust, integrity, dynamic, limitless possibilities, transition, energy, creative. We plan to expand in the future to be international.

There will also be a contest running for stationary. Please check that section, as well.

***Black is 80-90 percent black. Not stark black

Tight timeline. Needs cards printed quickly!

Residential

```html
<!DOCTYPE html>
<html lang="en">
<head>
<meta charset="utf-8">
<title>Pinecrest Renovations – Business Card</title>
<link rel="stylesheet" href="https://fonts.googleapis.com/css2?family=Exo+2:wght@300;400;500&display=swap">
<style>
  :root {
    --backdrop: #6b6e78;
    --teal: #17a89b;
    --teal-pale: #e2f3f1;
    --white: #ffffff;
    --grey-band: #d3d4d6;
    --ink: #2b2f33;
    --ink-soft: #3c4447;
  }
  * { margin: 0; padding: 0; box-sizing: border-box; }
  html, body {
    width: 1200px; height: 1082px; overflow: hidden;
    background: var(--backdrop);
    font-family: "Exo 2", sans-serif;
  }
  .business-card {
    position: absolute; left: 75px; top: 241px;
    width: 1050px; height: 600px;
    background: var(--white);
    overflow: hidden;
    box-shadow: 0 12px 30px rgba(0,0,0,.25);
  }
  .top-band {
    position: absolute; left: 0; top: 0; width: 100%; height: 220px;
    background: var(--teal);
  }
  .holder {
    position: absolute; left: 360px; top: 160px;
    color: var(--ink-soft); white-space: nowrap;
    display: flex; align-items: baseline; gap: 16px;
  }
  .holder-name { font-size: 28px; font-weight: 500; letter-spacing: 3px; }
  .holder-divider { font-size: 28px; font-weight: 400; }
  .holder-role { font-size: 18px; font-weight: 400; letter-spacing: 2px; }
  .contact-panel {
    position: absolute; left: 0; top: 290px; width: 330px; height: 310px;
    background: var(--teal-pale);
  }
  .contact-list {
    position: absolute; left: 40px; top: 322px; list-style: none;
    color: var(--ink); font-size: 18px; font-weight: 400;
  }
  .contact-list li { display: flex; align-items: center; gap: 12px; height: 34px; }
  .contact-icon { width: 16px; height: 16px; flex: none; }
  .contact-icon * { fill: none; stroke: var(--ink); stroke-width: 1.6; }
  .grey-band {
    position: absolute; left: 560px; top: 430px; width: 490px; height: 170px;
    background: var(--grey-band);
  }
  .address {
    position: absolute; left: 600px; top: 498px;
    font-size: 24px; color: var(--ink); letter-spacing: .5px; white-space: nowrap;
  }
  .accent-shape { position: absolute; left: 0; top: 0; }
  .brand {
    position: absolute; left: 400px; top: 318px;
    display: flex; align-items: center; gap: 16px;
  }
  .brand-square { width: 26px; height: 26px; background: var(--teal); }
  .brand-name {
    font-size: 36px; font-weight: 400; letter-spacing: 2px;
    color: var(--ink); text-transform: uppercase; white-space: nowrap;
  }
</style>
</head>
<body>
  <div class="business-card">
    <div class="top-band"></div>
    <div class="holder">
      <span class="holder-name">ELENA MARSH</span>
      <span class="holder-divider">|</span>
      <span class="holder-role">GENERAL MANAGER</span>
    </div>

    <div class="contact-panel"></div>
    <div class="grey-band"></div>
    <svg class="accent-shape" width="1050" height="600" viewBox="0 0 1050 600" aria-hidden="true">
      <polygon points="330,600 560,430 560,600" fill="#17a89b" fill-opacity=".35"/>
      <polygon points="240,600 560,430 330,600" fill="#17a89b" fill-opacity=".18"/>
    </svg>

    <ul class="contact-list">
      <li>
        <svg class="contact-icon" viewBox="0 0 16 16"><path d="M4 2 L6 5 L5 7 Q7 10 9 11 L11 10 L14 12 L12 14 Q6 13 2 4 Z"/></svg>
        021 555 0147
      </li>
      <li>
        <svg class="contact-icon" viewBox="0 0 16 16"><rect x="4" y="1.5" width="8" height="13" rx="1.5"/><line x1="7" y1="12" x2="9" y2="12"/></svg>
        021 555 0148
      </li>
      <li>
        <svg class="contact-icon" viewBox="0 0 16 16"><rect x="2" y="6" width="12" height="8"/><rect x="4.5" y="2" width="7" height="4"/><line x1="5" y1="10" x2="11" y2="10"/></svg>
        021 555 0149
      </li>
      <li>
        <svg class="contact-icon" viewBox="0 0 16 16"><rect x="1.5" y="3.5" width="13" height="9"/><polyline points="1.5,3.5 8,9 14.5,3.5"/></svg>
        hello@pinecrestreno.com
      </li>
      <li>
        <svg class="contact-icon" viewBox="0 0 16 16"><circle cx="8" cy="8" r="6.5"/><ellipse cx="8" cy="8" rx="3" ry="6.5"/><line x1="1.5" y1="8" x2="14.5" y2="8"/></svg>
        www.pinecrestreno.com
      </li>
    </ul>

    <div class="brand">
      <span class="brand-square"></span>
      <span class="brand-name">Pinecrest Renovations</span>
    </div>

    <p class="address">42 Harbor View Road, Suite 3, West</p>
  </div>
</body>
</html>
```